Renewable energy company needs modern memorable marketing brochure

We have an 8 page marketing brochure which was created in house. This needs to be revamped and modernised to stand out from our competitors in Australia, Chile and the UK. The brochure should depict us as a professional and dynamic company and instil confidence in prospective clients that we do a professional job. Once the design is finalised we will need a country specific document in the correct language i.e. Spanish for Chile. We are happy to pay for these iterations. We have a company logo which we would like incorporated into the brochure and the colours from the logo utilised where appropriate in the overall design. I have uploaded our existing brochure for an example of the content that the brochure needs to have and can upload the images separately if they are needed. Images in the brochure need to be copyright free and we have lots of photos in-house. I have added all the images from the last brochure and also the text in Indesign so it can be copied easily if needed.

Target Market(s)

landowners and companies

Industry/Entity Type

It Company

Requirements
Must have
• A clean modern look with some colours taken from the logo colour. Be easy to print in various countries.

```html
<!DOCTYPE html>
<html lang="en">
<head>
<meta charset="utf-8">
<title>Solara Fields brochure cover spread</title>
<link href="https://fonts.googleapis.com/css2?family=Barlow:wght@400;500;600&family=Arimo:wght@400&display=swap" rel="stylesheet">
<style>
  :root {
    --canvas-bg: #e6e6e6;
    --paper: #ffffff;
    --ink: #231f20;
    --band-black: #1e1c1d;
    --band-grey: #a7a9ac;
    --accent-teal: #5fb3a7;
    --mark-grey: #9a9a9a;
    --text-body: #1a1a1a;
  }
  * { margin: 0; padding: 0; box-sizing: border-box; }
  html, body {
    width: 1200px; height: 1200px; overflow: hidden;
    background: var(--canvas-bg);
  }
  .spread {
    position: absolute; left: 40px; top: 204px;
    width: 1120px; height: 792px;
    display: flex;
    box-shadow: 0 2px 6px rgba(0,0,0,0.25);
  }
  .page {
    position: relative; width: 560px; height: 792px;
    background: var(--paper); overflow: hidden;
  }
  .page-art { position: absolute; inset: 0; width: 100%; height: 100%; }

  /* Back page: contact panel */
  .contact {
    position: absolute; left: 0; right: 0; top: 580px;
    font-family: "Arimo", Arial, sans-serif;
    font-size: 11px; line-height: 13.5px;
    color: var(--text-body); text-align: center;
  }
  .contact-heading { text-transform: uppercase; }
  .contact-region { margin-top: 21px; }
  .contact-people {
    display: flex; justify-content: center; gap: 30px; margin-top: 8px;
  }
  .contact-person { width: 200px; }
  .contact-company { margin-top: 20px; }

  /* Front cover */
  .brand {
    position: absolute; left: 280px; top: 38px;
    display: flex; align-items: center; gap: 14px;
  }
  .brand-dot {
    width: 76px; height: 76px; border-radius: 50%;
    background: var(--mark-grey);
  }
  .brand-name {
    font-family: "Barlow", sans-serif; font-weight: 400;
    font-size: 29px; line-height: 28px; color: var(--ink);
    letter-spacing: 0.5px; text-transform: uppercase;
  }
  .cover-title {
    position: absolute; left: 19px; top: 660px;
    font-family: "Barlow", sans-serif; color: var(--ink);
  }
  .cover-title h1 {
    font-weight: 600; font-size: 25px; line-height: 26px; text-transform: uppercase;
  }
  .cover-title p {
    font-weight: 500; font-size: 15px; line-height: 18px; text-transform: uppercase;
  }
  .cover-footer {
    position: absolute; left: 0; right: 0; bottom: 0; height: 42px;
    background: var(--band-black);
    display: flex; align-items: center; justify-content: center;
    padding-left: 40px;
  }
  .cover-footer span {
    font-family: "Arimo", Arial, sans-serif; font-size: 11px;
    letter-spacing: 4px; color: #ffffff;
  }
</style>
</head>
<body>
<main class="spread">
  <!-- Back page -->
  <section class="page page-back">
    <svg class="page-art" viewBox="0 0 646 915" preserveAspectRatio="none">
      <defs>
        <linearGradient id="vineyard-tones" x1="0" y1="0" x2="0" y2="1">
          <stop offset="0" stop-color="#d3dbe2"/>
          <stop offset="0.4" stop-color="#6e7f4a"/>
          <stop offset="0.6" stop-color="#b9a97a"/>
          <stop offset="1" stop-color="#6d8a3c"/>
        </linearGradient>
      </defs>
      <path fill="var(--band-grey)" d="M0 0 H646 V399 C560 454 450 459 350 439 C250 419 120 354 0 359 Z"/>
      <path fill="var(--paper)" d="M0 0 H646 V391 C560 446 450 451 350 431 C250 411 120 346 0 351 Z"/>
      <path fill="var(--band-black)" d="M0 0 H646 V385 C560 440 450 445 350 425 C250 405 120 340 0 345 Z"/>
      <path fill="var(--paper)" d="M0 0 H646 V362 C560 417 450 422 350 402 C250 382 120 317 0 322 Z"/>
      <path fill="url(#vineyard-tones)" role="img" aria-label="Photo: vineyard rows and a shady tree beside a solar farm"
            d="M0 0 H646 V350 C560 405 450 410 350 390 C250 370 120 305 0 310 Z"/>
    </svg>

    <div class="contact">
      <p class="contact-heading">Contact details</p>
      <p>If you are interested to learn more about securing a long term income stream<br>from a Solara Fields solar farm on your land please contact us</p>
      <p class="contact-region">Australia</p>
      <div class="contact-people">
        <div class="contact-person">
          <p>Tom Hale</p>
          <p>Business Development Associate</p>
          <p>tom.hale@solarafields.com.au</p>
          <p>+61 (0) 400 000 111</p>
        </div>
        <div class="contact-person">
          <p>Ben Carrow</p>
          <p>Business Development Associate</p>
          <p>ben.carrow@solarafields.com.au</p>
          <p>+61 (0) 400 000 222</p>
        </div>
      </div>
      <div class="contact-company">
        <p>Solara Fields PTY. Ltd.</p>
        <p>c/o Reed &amp; Vale Co, Level 2, 45 Harbour St, Newstead, Qld, 4000 Australia</p>
        <p>www.solarafields.com.au</p>
      </div>
    </div>
  </section>

  <!-- Front cover -->
  <section class="page page-cover">
    <div class="brand">
      <span class="brand-dot"></span>
      <p class="brand-name">Solara<br>Fields</p>
    </div>

    <svg class="page-art" viewBox="0 0 646 915" preserveAspectRatio="none">
      <defs>
        <linearGradient id="panel-tones" x1="0" y1="0" x2="0" y2="1">
          <stop offset="0" stop-color="#cdd6de"/>
          <stop offset="0.3" stop-color="#9fb0c2"/>
          <stop offset="0.45" stop-color="#5b7597"/>
          <stop offset="1" stop-color="#1f3a63"/>
        </linearGradient>
      </defs>
      <path fill="var(--band-grey)" d="M0 212 C120 152 260 152 400 202 C500 237 580 252 646 252 L646 738 C560 718 450 688 350 713 C250 738 100 748 0 688 Z"/>
      <path fill="none" stroke="var(--accent-teal)" stroke-width="2" d="M400 205 C500 240 580 255 646 255"/>
      <path fill="var(--paper)" d="M0 220 C120 160 260 160 400 210 C500 245 580 260 646 260 L646 730 C560 710 450 680 350 705 C250 730 100 740 0 680 Z"/>
      <path fill="var(--band-black)" d="M0 226 C120 166 260 166 400 216 C500 251 580 266 646 266 L646 722 C560 702 450 672 350 697 C250 722 100 732 0 672 Z"/>
      <path fill="url(#panel-tones)" role="img" aria-label="Photo: rows of solar panels reflecting a cloudy sky on a grassy field"
            d="M0 260 C120 200 260 200 400 250 C500 285 580 300 646 300 L646 690 C560 670 450 640 350 665 C250 690 100 700 0 640 Z"/>
    </svg>

    <div class="cover-title">
      <h1>Infinite Energy</h1>
      <p>Use your land to harvest energy from the sun</p>
    </div>

    <footer class="cover-footer"><span>www.solarafields.com.au</span></footer>
  </section>
</main>
</body>
</html>
```